Looking for a person and dog character for dog training school materials

I need two characters to use in my instructional materials for my online dog training program. I’m uploading examples for you of what I’m looking for. I’d like to stay away from details and stay similar to those. Once created, I’ll need the PDFs and printable designed as well. But let’s start with the characters.

Target Market(s)

Dog owners

Industry/Entity Type

Dog training 🐶

Font styles to use
Other font styles liked:
• Not needed

Colors

Designer to choose only greyscale colors for use in the design.

Requirements
Nice to have
• I’ve uploaded samples of what I’m looking for. I’d like basic movements to be shown - dog can sit, down, run, look up, jump etc. Person can point, bend, pet dog, etc. There will be a finite number of positions needed for both
Should not have
• Facial features - details. It will make it too hard to use them in different situations.

```html
<!DOCTYPE html>
<html lang="en">
<head>
<meta charset="utf-8">
<title>Dog Training School – Dog Character Design</title>
<link rel="stylesheet" href="https://fonts.googleapis.com/css2?family=Montserrat:wght@400;600;800&family=Poppins:wght@400;600&display=swap">
<style>
  :root {
    --lavender: #d8cceb;
    --plum: #85546d;
    --pink: #f05a78;
    --lime: #bfca55;
    --ink: #1d1b22;
    --figure: #4a4560;
    --white: #ffffff;
  }
  * { margin: 0; padding: 0; box-sizing: border-box; }
  html, body { width: 848px; height: 1200px; overflow: hidden; background: var(--white); }
  .page { position: relative; width: 848px; height: 1200px; background: var(--white); }

  .masthead { position: absolute; left: 0; top: 0; width: 848px; height: 324px; background: var(--lavender); }
  .masthead-frame { position: absolute; left: 0; top: 0; width: 848px; height: 324px; }
  .masthead-title {
    position: absolute; left: 0; width: 848px; text-align: center;
    font-family: "Montserrat", sans-serif; color: var(--white); line-height: 1;
  }
  .title-top { top: 60px; font-size: 58px; font-weight: 600; letter-spacing: -0.5px; }
  .title-main { top: 116px; font-size: 96px; font-weight: 800; letter-spacing: -1px; }
  .masthead-subtitle {
    position: absolute; left: 111px; top: 212px; width: 651px; height: 78px;
    display: flex; align-items: center; justify-content: center;
    font-family: "Montserrat", sans-serif; font-weight: 400; font-size: 33px;
    color: var(--white); letter-spacing: 0.5px;
  }

  .lesson { position: absolute; left: 0; width: 848px; height: 401px; background: var(--lavender); }
  .lesson-one { top: 345px; }
  .lesson-two { top: 766px; }

  .step-badge { position: absolute; left: 59px; top: 61px; width: 147px; height: 64px; }
  .step-number {
    position: absolute; left: 59px; top: 61px; width: 70px; height: 64px;
    display: flex; align-items: center; justify-content: center;
    font-family: "Montserrat", sans-serif; font-weight: 800; font-size: 46px; color: var(--white);
  }
  .step-text {
    position: absolute; left: 59px; top: 165px; width: 400px;
    font-family: "Poppins", sans-serif; font-size: 21px; line-height: 26.2px; color: var(--ink);
  }
  .scene { position: absolute; }
  .lesson-one .scene { left: 490px; top: 55px; width: 315px; height: 306px; }
  .lesson-two .scene { left: 502px; top: 68px; width: 291px; height: 279px; }
</style>
</head>
<body>
<main class="page">
  <header class="masthead">
    <svg class="masthead-frame" viewBox="0 0 848 324" aria-hidden="true">
      <polygon points="115,25 763,22 737,212 127,212" fill="var(--plum)" stroke="var(--white)" stroke-width="5" stroke-linejoin="round"/>
      <rect x="113" y="211" width="647" height="77" fill="var(--pink)" stroke="var(--white)" stroke-width="6" rx="2"/>
    </svg>
    <h1>
      <span class="masthead-title title-top">DOG TRAINING</span>
      <span class="masthead-title title-main">SCHOOL</span>
    </h1>
    <p class="masthead-subtitle">Dog Character Design</p>
  </header>

  <section class="lesson lesson-one">
    <svg class="step-badge" viewBox="0 0 147 64" aria-hidden="true">
      <polygon points="0,0 106,0 63,64 0,64" fill="var(--pink)"/>
      <rect x="111" y="33" width="35" height="31" fill="var(--white)"/>
    </svg>
    <span class="step-number">1</span>
    <p class="step-text">Lorem ipsum dolor sit amet, consect etur adipiscing elit, sed do eiusmod. Vitae aliquet nec ullamcorper sit amet risus nullam eget. Sed viverra tellus in hac habitasse platea dictumst eget sit amet tellus</p>
    <svg class="scene" viewBox="0 0 315 306" role="img" aria-label="Silhouette of a standing trainer pointing up while a dog sits looking up">
      <rect width="315" height="306" rx="24" fill="var(--figure)"/>
    </svg>
  </section>

  <section class="lesson lesson-two">
    <svg class="step-badge" viewBox="0 0 147 64" aria-hidden="true">
      <polygon points="0,0 106,0 63,64 0,64" fill="var(--lime)"/>
      <rect x="111" y="33" width="35" height="31" fill="var(--white)"/>
    </svg>
    <span class="step-number">2</span>
    <p class="step-text">Lorem ipsum dolor sit amet, consect etur adipiscing elit, sed do eiusmod. Vitae aliquet nec ullamcorper sit amet risus nullam eget. Sed viverra tellus in hac habitasse platea dictumst eget sit amet tellus</p>
    <svg class="scene" viewBox="0 0 291 279" role="img" aria-label="Silhouette of a kneeling trainer shaking paws with a sitting dog">
      <rect width="291" height="279" rx="24" fill="var(--figure)"/>
    </svg>
  </section>
</main>
</body>
</html>
```